Premium Gold Vodka Label Design

English ------------------- We need a label for a Vodka Bottle. Its a sparkling premium vodka with gold inside. The design should look premium. We tried it on our selves but it looks horrible. Therefore we need your help. The current name is glimora K, but we are open for any better suggestion. We attached the selfmade design. The label will be printed on the bottle. We have other design jobs for you (logo, other sorts)! English ------------------------ We need a label for a vodka bottle. This is a premium vodka which is offset with gold. The design should look like this. We have tried so far and failed. That is why we need your support. The name is so far glimora K. If you have better suggestions we would be pleased about other suggestions / ideas. In the appendix the failed design is stored. The label is to be applied by screen printing. In the case of good work follow-up projects are guaranteed (logo, other varieties, etc)!

Target Market(s)

USA

Colors

Designer to choose colors to be used in the design.

Requirements
Must have
• English ------------------------ The needed text is on our selfmade label that is attached. English ------------------------ The required texts are stored in the attached design.
Nice to have
• English ------------------------ Transparent places are allowed because we want to print the label on the bottom. English ------------------------ As the label is applied by screen printing, transparent areas are also possible.

```html
<!DOCTYPE html>
<html lang="en">
<head>
<meta charset="utf-8">
<title>Glimora Vodka – Label</title>
<link rel="stylesheet" href="https://fonts.googleapis.com/css2?family=Alegreya+Sans+SC:wght@800&family=Playfair+Display:wght@700&family=Oswald:wght@500&family=Libre+Baskerville:wght@700&display=swap">
<style>
  :root {
    --paper: #ffffff;
    --label-black: #141311;
    --rim-white: #ffffff;
    --gold: #e8bb4d;
    --gold-deep: #9a6a22;
    --gold-light: #f6d98c;
    --ink-white: #ffffff;
    --ink-dark: #3a2608;
  }
  html, body {
    margin: 0;
    width: 1200px;
    height: 1124px;
    overflow: hidden;
    background: var(--paper);
  }
  .canvas {
    position: relative;
    width: 1200px;
    height: 1124px;
  }
  .label {
    position: absolute;
    left: 360px;
    top: 288px;
    width: 428px;
    height: 540px;
  }
  .label__shape { fill: var(--label-black); }
  .label__rim { fill: none; stroke: var(--rim-white); stroke-width: 2.5; }
  .label__frame { fill: none; stroke: var(--gold); stroke-width: 4.5; }
  .badge__ring { fill: var(--label-black); stroke: var(--gold); stroke-width: 4; }
  .badge__inner { fill: none; stroke: var(--gold-light); stroke-width: 1.2; }
  .badge__text {
    font-family: "Libre Baskerville", serif;
    font-weight: 700;
    font-size: 25px;
    fill: var(--ink-white);
  }
  .brand-name {
    font-family: "Alegreya Sans SC", sans-serif;
    font-weight: 800;
    font-size: 60px;
    fill: var(--ink-white);
  }
  .product-type {
    font-family: "Playfair Display", serif;
    font-weight: 700;
    font-size: 78px;
    fill: var(--gold);
  }
  .process-line {
    font-family: "Alegreya Sans SC", sans-serif;
    font-weight: 800;
    font-size: 18px;
    fill: var(--ink-white);
  }
  .spec-line {
    font-family: "Alegreya Sans SC", sans-serif;
    font-weight: 800;
    font-size: 14px;
    fill: var(--ink-white);
  }
  .ribbon__band { fill: url(#ribbonGold); }
  .ribbon__tail { fill: url(#ribbonTail); }
  .ribbon__origin {
    font-family: "Oswald", sans-serif;
    font-weight: 500;
    font-size: 18px;
    fill: var(--ink-white);
  }
  .ribbon__tagline {
    font-family: "Oswald", sans-serif;
    font-weight: 500;
    font-size: 16px;
    fill: var(--ink-dark);
  }
</style>
</head>
<body>
<main class="canvas">
  <svg class="label" viewBox="0 0 428 540" xmlns="http://www.w3.org/2000/svg">
    <defs>
      <linearGradient id="ribbonGold" x1="0" y1="0" x2="1" y2="0">
        <stop offset="0" stop-color="#8a5a1a"/>
        <stop offset="0.3" stop-color="#e6b95a"/>
        <stop offset="0.55" stop-color="#f7dc93"/>
        <stop offset="0.8" stop-color="#c8913a"/>
        <stop offset="1" stop-color="#8a5a1a"/>
      </linearGradient>
      <linearGradient id="ribbonTail" x1="0" y1="0" x2="0" y2="1">
        <stop offset="0" stop-color="#c48b34"/>
        <stop offset="1" stop-color="#6e4512"/>
      </linearGradient>
      <linearGradient id="scrollTone" x1="0" y1="0" x2="0" y2="1">
        <stop offset="0" stop-color="#e9dcc0" stop-opacity="0.35"/>
        <stop offset="1" stop-color="#a5692c" stop-opacity="0.35"/>
      </linearGradient>
      <path id="originCurve" d="M 100,444 Q 214,462 328,444"/>
      <path id="taglineCurve" d="M 96,476 Q 214,496 332,476"/>
    </defs>

    <path class="label__shape" d="M0,40 C60,40 100,0 214,0 C328,0 368,40 428,40 L428,490 C368,490 328,540 214,540 C100,540 60,490 0,490 Z"/>
    <path class="label__rim" d="M8,48 C60,48 100,8 214,8 C328,8 368,48 420,48 L420,482 C368,482 328,532 214,532 C100,532 60,482 8,482 Z"/>
    <path class="label__frame" d="M20,60 C64,60 104,20 214,20 C324,20 364,60 408,60 L408,470 C364,470 324,520 214,520 C104,520 64,470 20,470 Z"/>

    <rect class="ornament ornament--left" role="img" aria-label="Gold filigree scrollwork ornament" x="44" y="48" width="136" height="152" rx="50" fill="url(#scrollTone)"/>
    <rect class="ornament ornament--right" role="img" aria-label="Gold filigree scrollwork ornament" x="248" y="48" width="136" height="152" rx="50" fill="url(#scrollTone)"/>

    <g class="badge">
      <circle class="badge__ring" cx="214" cy="116" r="48"/>
      <circle class="badge__inner" cx="214" cy="116" r="42"/>
      <text class="badge__text" x="214" y="125" text-anchor="middle">24kt</text>
    </g>

    <text class="brand-name" x="214" y="266" text-anchor="middle" textLength="300" lengthAdjust="spacingAndGlyphs">Glimora</text>
    <text class="product-type" x="214" y="336" text-anchor="middle" textLength="310" lengthAdjust="spacingAndGlyphs">VODKA</text>
    <text class="process-line" x="214" y="362" text-anchor="middle" textLength="180" lengthAdjust="spacingAndGlyphs">Distilled 8 Filtered</text>
    <text class="spec-line" x="214" y="388" text-anchor="middle" textLength="225" lengthAdjust="spacingAndGlyphs">40% Alc Vol  200ml  80Proof</text>

    <g class="ribbon">
      <path class="ribbon__tail" d="M48,404 L94,414 L98,466 L60,456 L70,432 Z"/>
      <path class="ribbon__tail" d="M380,404 L334,414 L330,466 L368,456 L358,432 Z"/>
      <path class="ribbon__band" d="M78,420 Q214,452 350,420 L346,472 Q214,504 82,472 Z"/>
      <text class="ribbon__origin"><textPath href="#originCurve" startOffset="50%" text-anchor="middle" textLength="210" lengthAdjust="spacingAndGlyphs">MADE IN GERMANY</textPath></text>
      <text class="ribbon__tagline"><textPath href="#taglineCurve" startOffset="50%" text-anchor="middle" textLength="196" lengthAdjust="spacingAndGlyphs">Premium Gold Sparkling</textPath></text>
    </g>
  </svg>
</main>
</body>
</html>
```